Chimney Service company needs new business card design

We need a updated business card with our new logo added. We provide a full range of chimney services throughout Vermont and New Hampshire. The business card will be one sided and color. Attached is our current business card another document showing all the information we would like on the card.
We dont like a lot of flashy colors.... here is a link to our website to get an idea of our branding www.flueguardianvt.example

Target Market(s)

homeowners

Industry/Entity Type

Business

Contact Information for Business Card

See attached sheet for content.

Font styles to use
Serif
Sans Serif

Requirements
Must have
• all information provided on separate sheet
Should not have
• Additional information that may clogg up design

```html
<!DOCTYPE html>
<html lang="en">
<head>
<meta charset="utf-8">
<title>Flue Guardian – Business Card</title>
<link rel="stylesheet" href="https://fonts.googleapis.com/css2?family=PT+Sans+Narrow:wght@400;700&display=swap">
<style>
  :root {
    --backdrop: #f1f1ef;
    --card-dark: #232224;
    --card-mid: #2f2c2e;
    --brick-tone: #3a3032;
    --band: #121112;
    --panel: #f4f4f2;
    --ink-light: #eceaea;
    --ink-dark: #2a2a2a;
    --accent: #8a2a26;
  }
  * { margin: 0; padding: 0; box-sizing: border-box; }
  html, body {
    width: 1200px; height: 836px; overflow: hidden;
    background: var(--backdrop);
    font-family: "PT Sans Narrow", "Arial Narrow", sans-serif;
  }
  .stage {
    width: 1200px; height: 836px;
    display: flex; align-items: center; justify-content: center;
  }
  .card {
    position: relative;
    width: 840px; height: 480px;
    background: linear-gradient(160deg, var(--card-mid) 0%, var(--card-dark) 60%, #1d1b1d 100%);
    overflow: hidden;
    box-shadow: 0 6px 24px rgba(0,0,0,0.12);
  }
  .brick-texture {
    position: absolute; left: 0; bottom: 0;
    width: 520px; height: 300px;
    background: linear-gradient(20deg, var(--brick-tone) 0%, rgba(58,48,50,0.55) 45%, rgba(58,48,50,0) 100%);
  }
  .logo-panel {
    position: absolute; top: 0; right: 0;
    width: 260px; height: 220px;
    background: var(--panel);
    display: flex; align-items: center; justify-content: center; gap: 12px;
  }
  .logo-mark {
    width: 30px; height: 30px;
    background: var(--accent);
  }
  .logo-name {
    font-size: 30px; font-weight: 700;
    color: var(--ink-dark);
    letter-spacing: 1px; text-transform: uppercase;
  }
  .services {
    position: absolute; top: 60px; right: 290px;
    list-style: none; text-align: right;
    color: var(--ink-light);
    font-size: 27px; line-height: 36px;
    letter-spacing: 0.5px; text-transform: uppercase;
  }
  .contact {
    position: absolute; right: 34px; top: 262px;
    text-align: right; color: var(--ink-light);
    font-size: 26px; line-height: 36px;
    letter-spacing: 0.5px;
  }
  .assurance-band {
    position: absolute; left: 0; bottom: 36px;
    width: 440px; padding: 12px 0 12px 26px;
    background: var(--band);
    color: #ffffff; font-weight: 700;
    font-size: 25px; line-height: 32px;
    letter-spacing: 0.5px; text-transform: uppercase;
  }
</style>
</head>
<body>
  <main class="stage">
    <section class="card">
      <div class="brick-texture" role="img" aria-label="Faint dark brick wall texture"></div>

      <div class="logo-panel">
        <span class="logo-mark"></span>
        <span class="logo-name">Flue Guardian</span>
      </div>

      <ul class="services">
        <li>Full Masonry Services</li>
        <li>Historic Chimney Restoration</li>
        <li>Stainless Steel Liners</li>
        <li>New Chimney Installations</li>
        <li>CHSA Certified Chimney Sweeps</li>
      </ul>

      <address class="contact" style="font-style: normal;">
        <div class="contact-phone">802-555-0147</div>
        <div class="contact-email">info@flueguardianvt.example</div>
        <div class="contact-web">www.flueguardianvt.example</div>
      </address>

      <div class="assurance-band">
        <div>Fully Insured-Free Estimates</div>
        <div>Family Owned and Operated</div>
      </div>
    </section>
  </main>
</body>
</html>
```